Phuket Thailand - Rental Villa Website

I have a villa for rent in Thailand and require a website - i need to demo pictures/walk through video, local attractions, villa facilities description plus seaonal rates and online booking.

Industry/Entity Type

Rental

Coding

Coded - Design and coding required

```html
<!DOCTYPE html>
<html lang="en">
<head>
<meta charset="utf-8">
<title>Andaman Cove Villa</title>
<link rel="stylesheet" href="https://fonts.googleapis.com/css2?family=Oswald:wght@400;500&family=Open+Sans:wght@400;600&family=Pathway+Gothic+One&display=swap">
<style>
:root{
  --blue:#1a8fd6;
  --blue-deep:#0c6fb3;
  --ink:#1d1d1d;
  --text:#6b6b6b;
  --white:#ffffff;
  --green:#1f7d1b;
  --green-bright:#0b9a0b;
  --green-dark:#0d6a0d;
  --sea:#35c4dc;
  --sand:#e9d6b8;
}
*{box-sizing:border-box;margin:0;padding:0}
html,body{width:1200px;height:2276px;overflow:hidden;background:var(--white)}
body{position:relative;font-family:"Open Sans",Arial,sans-serif;color:var(--ink)}
.abs{position:absolute}

/* hero */
.hero-photo{left:0;top:0;width:1200px;height:536px;
  background:linear-gradient(180deg,#8fc4e0 0%,#6fb6cf 30%,#3fb9c4 60%,#5fd2d8 80%,#9fe6ea 100%)}
.hero-cliff-left{left:0;top:0;width:420px;height:400px;
  background:linear-gradient(135deg,#1f3d22 0%,#3f7b3a 45%,rgba(90,150,80,0) 100%)}
.hero-cliff-right{right:0;top:0;width:420px;height:360px;
  background:linear-gradient(225deg,#2f5e2c 0%,#76a86a 45%,rgba(200,200,180,0) 100%)}
.hero-badge{left:393px;top:17px;width:416px;height:416px;border-radius:50%;
  background:rgba(255,255,255,.78);border:3px solid var(--blue);
  box-shadow:0 0 0 3px rgba(255,255,255,.8)}
.brand{left:393px;top:90px;width:416px;text-align:center;font-family:"Oswald",sans-serif;
  font-weight:500;font-size:42px;line-height:46px;color:var(--blue-deep);text-transform:uppercase}
.brand-rule{left:475px;top:203px;width:250px;height:4px;background:var(--ink)}
.tagline{left:420px;top:250px;width:360px;text-align:center;font-family:"Pathway Gothic One",sans-serif;
  font-size:29px;line-height:37px;color:var(--ink);text-transform:uppercase}

/* nav */
.nav-item{width:148px;height:148px;border-radius:50%;border:2px solid var(--blue);
  background:linear-gradient(180deg,rgba(255,255,255,.55) 0%,rgba(255,255,255,.55) 49%,var(--white) 49%);
  text-align:center;top:462px}
.nav-item svg{display:block;margin:20px auto 0;width:50px;height:46px}
.nav-label{display:block;margin-top:6px;font-size:26px;color:var(--ink)}
.nav-item.is-active .nav-label{color:var(--blue)}

/* section headings */
.section-icon{width:46px;height:46px;border-radius:50%;border:2px solid var(--blue);background:var(--white);
  display:flex;align-items:center;justify-content:center}
.section-icon svg{width:22px;height:22px}
.heading{left:0;width:1200px;display:flex;align-items:center;justify-content:center;gap:14px;
  font-family:"Oswald",sans-serif;font-size:33px;line-height:44px}
.heading .rule{width:104px;height:1px;background:var(--blue)}
.accent{color:var(--blue)}
.dark{color:var(--ink)}
.light{color:var(--white)}

/* welcome */
.welcome-copy{left:140px;top:708px;width:920px;text-align:center;font-size:15.5px;line-height:23px;color:var(--text)}
.welcome-copy p+p{margin-top:23px}

/* attractions */
.attractions-band{left:0;top:893px;width:1200px;height:417px;
  background:linear-gradient(180deg,#2f8fd8 0%,#1f7fc4 40%,#2a9bc9 75%,#3aa7c9 100%)}
.attraction-card{top:1009px;width:245px;height:260px;background:var(--white);padding:8px;
  box-shadow:0 3px 8px rgba(0,0,0,.35)}
.attraction-photo{width:229px;height:179px}
.attraction-title{margin-top:18px;text-align:center;font-size:23px;color:var(--blue)}

/* facilities */
.facility{top:1441px;width:238px;height:238px;border-radius:50%;border:2px solid var(--blue);padding:6px;background:var(--white)}
.facility-photo{position:relative;width:100%;height:100%;border-radius:50%;overflow:hidden}
.facility-caption{position:absolute;left:0;bottom:0;width:100%;height:82px;background:rgba(26,143,214,.85);
  display:flex;align-items:center;justify-content:center;text-align:center;
  font-family:"Oswald",sans-serif;font-size:23px;line-height:31px;color:var(--white);padding-bottom:10px}

/* rates */
.rates-band{left:0;top:1742px;width:1200px;height:386px;
  background:linear-gradient(180deg,#2a8a24 0%,#1c7a18 45%,#2f8a3a 80%,#3c8f55 100%)}
.rates-table{left:77px;top:1858px;width:1046px;border-collapse:collapse;color:var(--white)}
.rates-table th,.rates-table td{border:1px solid rgba(255,255,255,.85);text-align:center}
.rates-table th{background:var(--green-bright);height:51px;font-weight:400;font-size:26px}
.rates-table td{height:47px;font-size:21px;background:rgba(13,106,13,.35)}
.rates-table tbody tr:first-child td{background:rgba(13,90,13,.7)}
.rates-table th:first-child,.rates-table td:first-child{text-align:left;padding-left:17px}
.book-button{left:543px;top:2072px;width:112px;height:35px;background:var(--blue);color:var(--white);
  font-family:"Oswald",sans-serif;font-size:22px;line-height:35px;text-align:center}

/* footer */
.footer-band{left:0;top:2128px;width:1200px;height:148px;
  background:linear-gradient(180deg,var(--sea) 0%,#8fdde6 30%,#efe4cf 55%,var(--sand) 100%)}
.footer-nav a{position:absolute;top:2143px;font-size:17px;color:var(--ink);text-decoration:none}
.footer-nav a.is-active{color:var(--blue)}
.copyright{left:0;top:2221px;width:1200px;text-align:center;font-size:17px;color:var(--ink)}
.copyright strong{color:var(--blue);font-weight:600}
</style>
</head>
<body>

<header>
  <div class="abs hero-photo" role="img" aria-label="Tropical bay with turquoise water between green limestone cliffs"></div>
  <div class="abs hero-cliff-left" aria-hidden="true"></div>
  <div class="abs hero-cliff-right" aria-hidden="true"></div>
  <div class="abs hero-badge"></div>
  <div class="abs brand">Andaman Cove<br>Villa</div>
  <div class="abs brand-rule"></div>
  <p class="abs tagline">Lorem ipsum is simply dummy text of the printing and typesetting industry.</p>

  <nav>
    <a class="abs nav-item is-active" style="left:79px">
      <svg viewBox="0 0 50 46"><path d="M25 4 2 24h7v19h12V31h8v12h12V24h7L38 13V5h-6v3z" fill="#111"/></svg>
      <span class="nav-label">Home</span>
    </a>
    <a class="abs nav-item" style="left:258px">
      <svg viewBox="0 0 50 46"><path d="M33 4l9 9-24 24-11 3 3-11z" fill="#111"/><path d="M30 7l9 9" stroke="#fff" stroke-width="2"/></svg>
      <span class="nav-label">About</span>
    </a>
    <a class="abs nav-item" style="left:436px">
      <svg viewBox="0 0 50 46"><path d="M6 12h9l4-6h12l4 6h9v28H6z" fill="#111"/><circle cx="25" cy="25" r="9" fill="#fff"/><circle cx="25" cy="25" r="5.5" fill="#111"/></svg>
      <span class="nav-label">Gallery</span>
    </a>
    <a class="abs nav-item" style="left:616px">
      <svg viewBox="0 0 50 46"><path d="M25 42 6 22C-1 13 7 1 17 5c4 2 6 5 8 8 2-3 4-6 8-8 10-4 18 8 11 17z" fill="#111"/></svg>
      <span class="nav-label">Attraction</span>
    </a>
    <a class="abs nav-item" style="left:795px">
      <svg viewBox="0 0 50 46"><path d="M16 14c0-6 4-10 10-10s10 4 10 9c0 7-8 8-8 15h-6c0-9 8-10 8-15 0-2-2-4-4-4s-4 2-4 5z" fill="#111"/><rect x="22" y="33" width="6" height="7" fill="#111"/></svg>
      <span class="nav-label">Enquiry</span>
    </a>
    <a class="abs nav-item" style="left:973px">
      <svg viewBox="0 0 50 46"><rect x="4" y="8" width="42" height="30" rx="4" fill="#111"/><path d="M5 11l20 14 20-14" stroke="#fff" stroke-width="2.5" fill="none"/></svg>
      <span class="nav-label">Contact</span>
    </a>
  </nav>
</header>

<main>
  <section>
    <div class="abs section-icon" style="left:577px;top:599px">
      <svg viewBox="0 0 22 22"><path d="M11 2 1 11h3v9h5v-6h4v6h5v-9h3z" fill="#1a8fd6"/></svg>
    </div>
    <h1 class="abs heading" style="top:648px;font-weight:400"><span class="rule"></span><span><span class="accent">Welcome to</span> <span class="dark">ANDAMAN COVE VILLA</span></span><span class="rule"></span></h1>
    <div class="abs welcome-copy">
      <p>Lorem Ipsum is simply dummy text of the printing and typesetting industry. Lorem Ipsum has been the industry's standard dummy text ever since the 1500s, when an unknown printer took a galley to make a type specimen book. It has survived not only five centuries.</p>
      <p>Lorem Ipsum is simply dummy text of the printing and typesetting industry. Lorem Ipsum has been the industry's standard dummy text ever since the 1500s, when an unknown printer took a galley of type and scrambled.</p>
    </div>
  </section>

  <section>
    <div class="abs attractions-band" role="img" aria-label="Blue sea and sky with an island shoreline"></div>
    <div class="abs section-icon" style="left:577px;top:902px">
      <svg viewBox="0 0 22 22"><path d="M11 1a7 7 0 0 0-7 7c0 5 7 13 7 13s7-8 7-13a7 7 0 0 0-7-7z" fill="#1a8fd6"/><circle cx="11" cy="8" r="2.7" fill="#fff"/></svg>
    </div>
    <h2 class="abs heading" style="top:952px;font-weight:400"><span class="rule" style="background:#fff"></span><span><span class="light">Thailand</span> <span class="dark">Attraction</span></span><span class="rule" style="background:#fff"></span></h2>

    <article class="abs attraction-card" style="left:77px">
      <div class="attraction-photo" role="img" aria-label="Turquoise lagoon with green cliffs" style="background:linear-gradient(180deg,#7fb8e0 0%,#4f8f4a 45%,#4fd0d6 70%,#a8ecee 100%)"></div>
      <h3 class="attraction-title" style="font-weight:400">Popular Place</h3>
    </article>
    <article class="abs attraction-card" style="left:344px">
      <div class="attraction-photo" role="img" aria-label="Beach crowded with visitors beneath rocky islands" style="background:linear-gradient(180deg,#9cc8e8 0%,#5f7f4f 40%,#7fb8b0 60%,#d8c4a0 100%)"></div>
      <h3 class="attraction-title" style="font-weight:400">Thailand Special</h3>
    </article>
    <article class="abs attraction-card" style="left:610px">
      <div class="attraction-photo" role="img" aria-label="Lounge chair on a sunny beach with water bungalows" style="background:linear-gradient(180deg,#c8dff0 0%,#8fcfe0 40%,#7a5a3f 65%,#efe6d6 100%)"></div>
      <h3 class="attraction-title" style="font-weight:400">Prestigious Linda</h3>
    </article>
    <article class="abs attraction-card" style="left:880px">
      <div class="attraction-photo" role="img" aria-label="Traditional pavilion beside a green garden pond" style="background:linear-gradient(180deg,#dfe8e0 0%,#8f5a3a 35%,#5f7f3f 65%,#6f9a3f 100%)"></div>
      <h3 class="attraction-title" style="font-weight:400">Prestigious Linda</h3>
    </article>
  </section>

  <section>
    <div class="abs section-icon" style="left:577px;top:1332px">
      <svg viewBox="0 0 22 22"><rect x="5" y="1" width="12" height="20" rx="1" fill="#1a8fd6"/><g fill="#fff"><rect x="7.5" y="4" width="2.5" height="2.5"/><rect x="12" y="4" width="2.5" height="2.5"/><rect x="7.5" y="9" width="2.5" height="2.5"/><rect x="12" y="9" width="2.5" height="2.5"/><rect x="9.5" y="15" width="3" height="6"/></g></svg>
    </div>
    <h2 class="abs heading" style="top:1380px;font-weight:400"><span class="rule"></span><span><span class="accent">Villa</span> <span class="dark">Facilities</span></span><span class="rule"></span></h2>

    <article class="abs facility" style="left:124px">
      <div class="facility-photo" role="img" aria-label="Ocean front bedroom with sofas and sheer curtains" style="background:linear-gradient(180deg,#5a4f4a 0%,#c8bfb4 45%,#8a7f76 100%)">
        <h3 class="facility-caption" style="font-weight:400">Ocean Front<br>Rooms</h3>
      </div>
    </article>
    <article class="abs facility" style="left:480px">
      <div class="facility-photo" role="img" aria-label="Infinity pool overlooking the sea" style="background:linear-gradient(180deg,#8fa09a 0%,#b8c4c0 35%,#6fa0b0 60%,#3f7f9a 100%)">
        <h3 class="facility-caption" style="font-weight:400">Pool Villa</h3>
      </div>
    </article>
    <article class="abs facility" style="left:837px">
      <div class="facility-photo" role="img" aria-label="Candlelit table set with wine glasses" style="background:linear-gradient(180deg,#5a3a1f 0%,#a8743f 40%,#4f3fa0 70%,#2f2a4f 100%)">
        <h3 class="facility-caption" style="font-weight:400">Private Dining</h3>
      </div>
    </article>
  </section>

  <section>
    <div class="abs rates-band" role="img" aria-label="Green tropical shoreline with longtail boats"></div>
    <div class="abs section-icon" style="left:577px;top:1759px">
      <svg viewBox="0 0 22 22"><rect x="2" y="4" width="18" height="16" rx="1" fill="#1a8fd6"/><rect x="6" y="1.5" width="2" height="5" fill="#1a8fd6"/><rect x="14" y="1.5" width="2" height="5" fill="#1a8fd6"/><g fill="#fff"><rect x="5" y="9" width="3" height="3"/><rect x="9.5" y="9" width="3" height="3"/><rect x="14" y="9" width="3" height="3"/><rect x="5" y="14" width="3" height="3"/><rect x="9.5" y="14" width="3" height="3"/></g></svg>
    </div>
    <h2 class="abs heading" style="top:1806px;font-weight:400;gap:4px"><span class="rule" style="background:#fff"></span><span><span class="light">Seasonal</span> <span class="dark">Rates</span></span><span class="rule" style="background:#fff"></span></h2>

    <table class="abs rates-table">
      <colgroup><col style="width:254px"><col style="width:157px"><col style="width:160px"><col style="width:158px"><col style="width:157px"><col style="width:160px"></colgroup>
      <thead><tr><th>Seasonal rates</th><th>max. occ.</th><th>Christmas</th><th>Winter</th><th>Summer</th><th>normal</th></tr></thead>
      <tbody>
        <tr><td>standard</td><td>2</td><td>$140</td><td>$120</td><td>$110</td><td>$100</td></tr>
        <tr><td>Superior</td><td>2</td><td>$180</td><td>$160</td><td>$150</td><td>$140</td></tr>
        <tr><td>Delux</td><td>2+1</td><td>$240</td><td>$220</td><td>$200</td><td>$190</td></tr>
      </tbody>
    </table>
    <a class="abs book-button">Book Now</a>
  </section>
</main>

<footer>
  <div class="abs footer-band" role="img" aria-label="Sandy beach with seashells and starfish by the sea"></div>
  <nav class="footer-nav">
    <a class="is-active" style="left:317px">Home</a>
    <a style="left:408px">About</a>
    <a style="left:499px">Gallery</a>
    <a style="left:597px">Attraction</a>
    <a style="left:719px">Enquiry</a>
    <a style="left:823px">Contact</a>
  </nav>
  <p class="abs copyright">© <strong>ANDAMAN COVE VILLA</strong> - 2015. All Rights Reserved.</p>
</footer>

</body>
</html>
```